COMPETITION TITLE:
Premium Skincare Packaging Design for Modern Hydration Beauty Brand
ABOUT THE PROJECT
We are developing a new skincare brand called VELORENA.
We are looking for a sophisticated and commercially strong packaging design direction for our initial skincare soft launch.
The brand positioning is:
* modern premium skincare
* hydration-focused
* wellness-oriented
* calming and elegant
* emotionally reassuring
* modern feminine skincare
* premium online beauty brand
The products are designed around hydration, skin comfort and modern skincare rituals.
The brand is inspired by modern hydration and skin wellness for people adapting between warmer and colder climates. The visual direction should therefore feel emotionally warm, comforting and restorative while remaining modern, refined and internationally premium rather than overtly cultural or decorative.
WHAT WE NEED
We are primarily seeking the VISUAL DIRECTION and PACKAGING IDENTITY for one hero product:
LIGHT MOISTURISING DAY CREAM
The winning visual direction will later be adapted across additional products within the range, including:
* Brightening Eye Cream
* Hydrating Mist / Toner
Therefore we are looking for a cohesive skincare brand identity system rather than unrelated individual designs.
IMPORTANT PACKAGING INFORMATION
The product packaging is:
* white plastic pump dispenser bottle
* transparent clear plastic lid
* outer cardboard carton/box
Bottle dimensions:
* diameter: 30mm
* total height including lid: 147mm
* bottle body height: approx. 120mm
* transparent lid height: approx. 27mm
Outer carton dimensions:
* height: 150mm
* width: 40mm x 35mm
IMPORTANT:
The packaging itself is minimalist and lightweight, therefore the LABEL DESIGN and OVERALL BRAND DIRECTION should visually elevate the product and make it feel:
* premium
* substantial
* calming
* elegant
* modern
* trustworthy
* emotionally warm
* intentional
The design should help the packaging feel significantly more premium than standard mass-market skincare.
FILES PROVIDED
We are providing:
* bottle label template
* outer box template
* logo/icon
* packaging dimensions
The supplied logo/icon should be retained conceptually, however designers may professionally refine and recreate/vectorise the artwork where required for packaging consistency and premium presentation.
At this stage we are NOT looking for final technical production artwork.
We are primarily looking for:
* visual direction
* typography
* colour palette
* premium skincare aesthetic
* realistic product mockups
IMPORTANT WEBSITE NOTE
A current website link may be provided for background information only.
Please DO NOT take heavy visual inspiration from the existing website design, as the website itself is expected to evolve in the future alongside the packaging direction.
The packaging design should therefore LEAD the future visual identity of the brand rather than follow the current website styling.
DESIGN STYLE
We are looking for:
* modern premium wellness skincare
* understated luxury
* elegant typography
* emotionally warm but clean branding
* hydration-focused beauty aesthetic
* premium online skincare look
The product should feel:
* calming when held
* emotionally reassuring rather than clinical
* modern wellness rather than minimalist pharmacy
* elegant but human rather than cold luxury
* comforting and restorative rather than cosmetic-only
Subtle texture, tonal layering and sophisticated visual depth are encouraged where appropriate.
Designers are encouraged to create a recognisable and distinctive visual identity rather than generic minimalist skincare packaging.
PLEASE AVOID
* gold luxury clichés
* ornate decorative themes
* floral overload
* influencer-style beauty branding
* overly clinical pharmacy aesthetics
* generic Canva-style layouts
* packaging that feels cold or sterile
STYLE REFERENCES
Please take inspiration from brands such as:
* Mirven
* Plume Beauty
* Coraval
* Beauty of Dallith
We particularly like:
* elegant spacing
* clean premium typography
* calm colour palettes
* subtle luxury
* modern hydration skincare aesthetics
COLOUR DIRECTION
Preferred tones include:
* warm ivory
* soft cream
* muted blush
* sand
* charcoal typography
* subtle deep plum accents
* restrained muted rose-gold accents
Please avoid:
* neon colours
* excessive metallic effects
* harsh black-and-white pharmacy styling
* very dark packaging
IMPORTANT DESIGN NOTE
The slim vertical packaging should feel intentionally elegant and premium rather than small or sample-sized.
The label design should visually elongate and elevate the packaging.
LOGO
An existing logo/icon is provided and should be retained and integrated into the design direction rather than completely redesigned.
DELIVERABLES
We are looking for:
* one fully developed hero product design
* realistic bottle + outer box mockups
* coordinated visual direction suitable for future product extensions
* typography and colour direction
* editable source files
The final approved visual system will later be adapted across additional products within the range.
BRAND NAME
VELORENA
OPTIONAL TAGLINE DIRECTION
Tideshift Balance Hydration
Updates
Thank you everyone for the submissions so far — there are some very strong directions emerging.
A few important thoughts as the project develops:
We are looking not only for attractive skincare labels, but for a distinctive and recognisable BRAND IDENTITY that could grow with the business over time across future packaging formats including larger cartons, jars and premium skincare packaging.
One area we would particularly encourage designers to explore further is refinement/elevation of the existing logo/icon. We would like to retain the core rose/circle concept, however subtle refinement, balance, geometry, typography pairing and premium presentation are encouraged where appropriate.
The strongest directions for us so far are those that feel:
* emotionally warm rather than clinical
* modern premium wellness rather than generic minimal skincare
* calming and reassuring when viewed or held
* elegant and distinctive rather than trend-driven
* premium without relying on gold luxury clichés
We are especially interested in designs that create a memorable visual identity system rather than simply placing text onto a white skincare bottle.
Subtle tonal layering, refined typography, understated sophistication and intelligent visual restraint are all encouraged.
Many thanks again and we are very excited to see the next round of directions develop.

```html
<!DOCTYPE html>
<html lang="en">
<head>
<meta charset="utf-8">
<title>VELORENA Light Moisturising Day Cream – Packaging</title>
<link rel="stylesheet" href="https://fonts.googleapis.com/css2?family=Inter:wght@200;700&family=Open+Sans:wdth,wght@75..100,400..600&display=swap">
<style>
  :root{
    --backdrop:#dddcda;
    --ivory:#f7f1e8;
    --cream:#f5ebe1;
    --blush:#f4dbcf;
    --plum:#7b2f4b;
    --charcoal:#3b3432;
    --line:#5a5250;
    --mark-fill:#ead3c9;
  }
  *{box-sizing:border-box;margin:0;padding:0}
  html,body{width:1100px;height:1200px;overflow:hidden}
  body{background:var(--backdrop);position:relative;font-family:"Open Sans",sans-serif;color:var(--charcoal)}

  .panel{
    position:absolute;overflow:hidden;
    background:linear-gradient(180deg,var(--ivory) 0%,var(--cream) 30%,var(--blush) 60%,var(--cream) 82%,var(--ivory) 100%);
  }
  .panel--label{left:284px;top:443px;width:186px;height:679px}
  .panel--carton{left:556px;top:176px;width:271px;height:937px}

  .headline{position:absolute;left:0;top:0;width:100%;height:100%;font-size:0}
  .headline svg{position:absolute;left:0;top:0;width:100%;height:100%;overflow:visible}
  .headline text{font-family:"Inter",sans-serif;fill:var(--plum)}
  .headline .strong{font-weight:700}
  .headline .light{font-weight:200}

  .brand{position:absolute;display:flex;flex-direction:column;align-items:center;text-align:center}
  .brand__dot{display:block;border-radius:50%;background:var(--mark-fill)}
  .brand__name{font-weight:400;letter-spacing:.12em;line-height:1;color:var(--charcoal);white-space:nowrap}

  .tagline{position:absolute;font-weight:600;font-stretch:85%;line-height:1.2;color:var(--plum);text-align:right;white-space:nowrap}
  .lede{position:absolute;text-align:right;color:var(--charcoal);white-space:nowrap}

  .claims{position:absolute;display:flex;list-style:none}
  .claim{display:flex;flex-direction:column;align-items:center}
  .claim svg{fill:none;stroke:var(--line);stroke-width:1.3}
  .claim span{text-align:center;color:var(--charcoal);white-space:nowrap}

  .volume{position:absolute;color:var(--charcoal);line-height:1}

  /* carton */
  .panel--carton .brand{left:118px;top:41px;width:140px}
  .panel--carton .brand__dot{width:78px;height:78px}
  .panel--carton .brand__name{margin-top:11px;font-size:17px}
  .panel--carton .tagline{right:23px;top:186px;font-size:13px}
  .panel--carton .lede{right:23px;top:212px;font-size:11.5px;line-height:16px}
  .panel--carton .claims{left:103px;top:261px}
  .panel--carton .claim{width:39px}
  .panel--carton .claim svg{width:27px;height:27px}
  .panel--carton .claim span{margin-top:7px;font-size:9.5px;line-height:10px}
  .panel--carton .volume{right:23px;bottom:38px;font-size:19px}

  /* bottle label */
  .panel--label .brand{left:77px;top:42px;width:120px}
  .panel--label .brand__dot{width:54px;height:54px}
  .panel--label .brand__name{margin-top:8px;font-size:12px}
  .panel--label .tagline{right:15px;top:155px;font-size:9.5px}
  .panel--label .lede{right:15px;top:176px;font-size:9px;font-stretch:90%;line-height:14px}
  .panel--label .claims{left:75px;top:217px}
  .panel--label .claim{width:27px}
  .panel--label .claim svg{width:20px;height:20px}
  .panel--label .claim span{margin-top:6px;font-size:7px;font-stretch:85%;line-height:9px}
  .panel--label .volume{right:14px;bottom:40px;font-size:12px}
</style>
</head>
<body>

<svg width="0" height="0" style="position:absolute">
  <defs>
    <symbol id="icon-badge" viewBox="0 0 36 36"><ellipse cx="18" cy="18" rx="16" ry="11"/><ellipse cx="18" cy="18" rx="13" ry="8.5"/></symbol>
    <symbol id="icon-leaf" viewBox="0 0 36 36"><path d="M18 3C9 11 9 25 18 33C27 25 27 11 18 3Z"/><path d="M18 8V33M18 16l-5-4M18 16l5-4M18 23l-6-4M18 23l6-4"/></symbol>
    <symbol id="icon-sprout" viewBox="0 0 36 36"><path d="M18 33V12"/><path d="M18 12C14 9 14 5 18 2C22 5 22 9 18 12Z"/><path d="M18 24C12 24 8 20 7 16C13 16 17 19 18 24Z"/><path d="M18 24C24 24 28 20 29 16C23 16 19 19 18 24Z"/></symbol>
    <symbol id="icon-acorn" viewBox="0 0 36 36"><path d="M18 3V8"/><path d="M7 14C7 9 12 8 18 8C24 8 29 9 29 14Z"/><path d="M9 14C9 24 13 31 18 33C23 31 27 24 27 14"/></symbol>
  </defs>
</svg>

<section class="panel panel--label" aria-label="Bottle label">
  <h1 class="headline">
    <svg viewBox="0 0 186 679">
      <g transform="translate(0,640) rotate(-90)">
        <text class="strong" x="0" y="49" font-size="41" textLength="598" lengthAdjust="spacingAndGlyphs">LIGHT MOISTURISING</text>
        <text class="light" x="0" y="102" font-size="56" textLength="306" lengthAdjust="spacingAndGlyphs">DAY CREAM</text>
      </g>
    </svg>
  </h1>
  <div class="brand"><span class="brand__dot"></span><span class="brand__name">VELORENA</span></div>
  <p class="tagline">Tideshift Balance Hydration</p>
  <p class="lede">Lightweight daily hydration<br>for calm, comfortable skin</p>
  <ul class="claims">
    <li class="claim"><svg><use href="#icon-badge"/></svg><span>Certified<br>Natural</span></li>
    <li class="claim"><svg><use href="#icon-leaf"/></svg><span>Vegan<br>Friendly</span></li>
    <li class="claim"><svg><use href="#icon-sprout"/></svg><span>Gluten<br>Free</span></li>
    <li class="claim"><svg><use href="#icon-acorn"/></svg><span>Nut<br>Free</span></li>
  </ul>
  <p class="volume">50 ml</p>
</section>

<section class="panel panel--carton" aria-label="Carton front panel">
  <h2 class="headline">
    <svg viewBox="0 0 271 937">
      <g transform="translate(0,895) rotate(-90)">
        <text class="strong" x="0" y="76" font-size="72" textLength="747" lengthAdjust="spacingAndGlyphs">LIGHT MOISTURISING</text>
        <text class="light" x="0" y="145" font-size="74" textLength="388" lengthAdjust="spacingAndGlyphs">DAY CREAM</text>
      </g>
    </svg>
  </h2>
  <div class="brand"><span class="brand__dot"></span><span class="brand__name">VELORENA</span></div>
  <p class="tagline">Tideshift Balance Hydration</p>
  <p class="lede">Lightweight daily hydration<br>for calm, comfortable skin</p>
  <ul class="claims">
    <li class="claim"><svg><use href="#icon-badge"/></svg><span>Certified<br>Natural</span></li>
    <li class="claim"><svg><use href="#icon-leaf"/></svg><span>Vegan<br>Friendly</span></li>
    <li class="claim"><svg><use href="#icon-sprout"/></svg><span>Gluten<br>Free</span></li>
    <li class="claim"><svg><use href="#icon-acorn"/></svg><span>Nut<br>Free</span></li>
  </ul>
  <p class="volume">50 ml</p>
</section>

</body>
</html>
```